KVM WordPress Design Project

• Current web site is www.TheMarbleAtlasHub.example
• Design client rejected is http://198.51.100.47/~kvm/
• Need Home Page design
o Would like 4 sections in the body of the page to describe key services and link to pages
• Prefers gray or black background. So font would need to be white or light and probably bold to make it easier to read.
• Sites the client really likes
o Zyq.example
o Veltrimosa-usa.example (Likes 3 sections. Likes black navigation bar.)
• Sites the client doesn’t like
o Harlowe.example
o Bxtmag.example
o Sites that scream “This is a WordPress site!”
• Logo – Client is getting a transparent background logo with white lettering. It’s OK to use current logo for the design.
Updates

Great options!  I have emailed the designs to my client for review.  Will have feedback for you asap.

The client has postponed the decision until Thursday. They have a big event tomorrow that is distracting them.  I'll get back to you asap!

Thank you all for very excellent designs. The client has made a choice. This was my first ArtHiveHub project. It worked so well that I will be back!

Target Market(s)

architects, general contractors, interior designers

Requirements
Must have
• PSD files of final design.

Top navigation

Medium gray or dark background.

4 sections on Home Page to describe top 4 services and link to those pages of site. Sections need to be clearly distinguished like the boxes on veltrimosa-usa. Can't be 4 sections on solid gray background. Sections need to "pop."

Should not have
• Design must go across the page. No sides like the design at
http://198.51.100.47/~kvm

```html
<!DOCTYPE html>
<html lang="en">
<head>
<meta charset="utf-8">
<title>The Marble Atlas Hub</title>
<link rel="stylesheet" href="https://fonts.googleapis.com/css2?family=Arimo:wght@400;700&display=swap">
<style>
:root{
  --bg-dark:#1f1f1f;
  --nav-dark:#2b2b2b;
  --nav-line:#444;
  --accent:#f05a1a;
  --accent-deep:#e2401a;
  --card-bg:rgba(10,10,10,0.9);
  --news-bg:#f0f0f0;
  --text-light:#ffffff;
  --text-muted:#c8c8c8;
  --text-dark:#333333;
  --social-a:#3a5a9a;
  --social-b:#4fb6e8;
}
*{margin:0;padding:0;box-sizing:border-box}
html,body{width:1200px;height:960px;overflow:hidden}
body{font-family:"Arimo",Arial,sans-serif;background:var(--bg-dark);position:relative;color:var(--text-light)}
.site-header{position:absolute;left:0;top:0;width:1200px;height:108px;background:var(--bg-dark)}
.hero{position:absolute;left:0;top:108px;width:1200px;height:704px;
  border-top:5px solid #e8e8e8;
  background:
   radial-gradient(ellipse at 60% 95%,rgba(255,205,90,.75),transparent 55%),
   radial-gradient(ellipse at 80% 15%,rgba(255,220,160,.5),transparent 30%),
   linear-gradient(100deg,#7a5a3a 0%,#4a2e1c 30%,#6b4326 55%,#3e2a1e 80%,#5a3a24 100%)}
.brand{position:absolute;left:90px;top:13px;width:425px;height:145px;background:#fff;
  display:flex;align-items:center;justify-content:center;gap:12px;z-index:2;box-shadow:0 1px 3px rgba(0,0,0,.4)}
.brand-mark{width:26px;height:26px;background:var(--accent)}
.brand-name{font-size:34px;font-weight:700;color:#111;letter-spacing:1px;line-height:1.1;text-transform:uppercase}
.phone{position:absolute;right:88px;top:17px;font-size:20px;color:var(--text-light)}
.search{position:absolute;left:942px;top:56px;width:169px;height:29px;background:#f4f4f4;border:1px solid #ccc;
  font-size:11px;color:#333;padding:8px 12px}
.search svg{position:absolute;right:8px;top:6px}
.main-nav{position:absolute;left:515px;top:113px;width:596px;height:44px;
  background:linear-gradient(#3a3a3a,#222);display:flex;justify-content:flex-end;z-index:2}
.main-nav a{display:flex;align-items:center;justify-content:center;height:44px;font-size:15px;color:var(--text-light);
  text-decoration:none;border-left:1px solid var(--nav-line)}
.main-nav a.active{background:linear-gradient(#f7772a,var(--accent-deep));border-left:none}
.services{position:absolute;left:89px;top:608px;width:1022px;display:flex;gap:13px}
.service{width:246px;height:190px;background:var(--card-bg);border-top:3px solid var(--accent-deep);padding:16px 14px 0 14px}
.service h2{font-size:16.5px;font-weight:400;color:var(--accent);margin-bottom:9px}
.service p{font-size:13.5px;line-height:21px;text-align:justify;padding:0 2px}
.service .more{display:flex;align-items:center;gap:7px;margin-top:21px;font-size:14px;color:var(--text-light);text-decoration:none;padding-left:2px}
.news{position:absolute;left:0;top:812px;width:1200px;height:56px;background:var(--news-bg);
  display:flex;align-items:center}
.news-icon{margin-left:131px;width:30px;height:24px;background:#cfcfcf;transform:rotate(-14deg)}
.news h3{margin-left:13px;font-size:17px;font-weight:400;color:var(--accent-deep)}
.news p{margin-left:29px;font-size:13px;color:var(--text-dark)}
.site-footer{position:absolute;left:0;top:868px;width:1200px;height:92px;background:var(--bg-dark)}
.footer-nav{position:absolute;left:91px;top:24px;font-size:12.5px;color:var(--text-muted)}
.footer-nav a{color:var(--text-muted);text-decoration:none}
.footer-nav span{margin:0 9px}
.copyright{position:absolute;left:91px;top:57px;font-size:12.5px;color:var(--text-muted);word-spacing:2px}
.social{position:absolute;left:1055px;top:37px;display:flex;gap:7px}
.social span{width:24px;height:24px;border-radius:4px}
.social .s1{background:var(--social-a)}
.social .s2{background:var(--social-b)}
</style>
</head>
<body>
<header class="site-header">
  <div class="brand"><span class="brand-mark"></span><span class="brand-name">The Marble<br>Atlas Hub</span></div>
  <div class="phone">Call : 555.014.2286</div>
  <div class="search">Search
    <svg width="16" height="16" viewBox="0 0 16 16"><circle cx="6" cy="6" r="4.5" fill="none" stroke="#222" stroke-width="2.2"/><line x1="9.5" y1="9.5" x2="14.5" y2="14.5" stroke="#222" stroke-width="3"/></svg>
  </div>
</header>
<nav class="main-nav">
  <a class="active" href="#" style="width:73px">Home</a>
  <a href="#" style="width:74px">About</a>
  <a href="#" style="width:117px">Associations</a>
  <a href="#" style="width:94px">Products</a>
  <a href="#" style="width:95px">Calendar</a>
  <a href="#" style="width:95px">Contact</a>
</nav>
<section class="hero" role="img" aria-label="Photo of a warmly lit library interior with tall wooden bookshelves"></section>
<section class="services">
  <article class="service"><h2>BINDER FINDER</h2><p>Temporibus debitis amat aut rerum Itaque earum rerum hic tenetur a sapiente delectus, ut aut reiciendis voluptatibus maiores.</p><a class="more" href="#"><svg width="8" height="9" viewBox="0 0 8 9"><line x1="1" y1="0" x2="1" y2="9" stroke="#fff" stroke-width="1.5"/><path d="M3 0 L8 4.5 L3 9Z" fill="#fff"/></svg>MORE</a></article>
  <article class="service"><h2>BOX LUNCH BUREAU</h2><p>Temporibus debitis amat aut rerum Itaque earum rerum hic tenetur a sapiente delectus, ut aut reiciendis voluptatibus maiores.</p><a class="more" href="#"><svg width="8" height="9" viewBox="0 0 8 9"><line x1="1" y1="0" x2="1" y2="9" stroke="#fff" stroke-width="1.5"/><path d="M3 0 L8 4.5 L3 9Z" fill="#fff"/></svg>MORE</a></article>
  <article class="service"><h2>DONUTS &amp; A DEMO</h2><p>Temporibus debitis amat aut rerum Itaque earum rerum hic tenetur a sapiente delectus, ut aut reiciendis voluptatibus maiores.</p><a class="more" href="#"><svg width="8" height="9" viewBox="0 0 8 9"><line x1="1" y1="0" x2="1" y2="9" stroke="#fff" stroke-width="1.5"/><path d="M3 0 L8 4.5 L3 9Z" fill="#fff"/></svg>MORE</a></article>
  <article class="service"><h2>COOKIES &amp; QUESTIONS</h2><p>Temporibus debitis amat aut rerum Itaque earum rerum hic tenetur a sapiente delectus, ut aut reiciendis voluptatibus maiores.</p><a class="more" href="#"><svg width="8" height="9" viewBox="0 0 8 9"><line x1="1" y1="0" x2="1" y2="9" stroke="#fff" stroke-width="1.5"/><path d="M3 0 L8 4.5 L3 9Z" fill="#fff"/></svg>MORE</a></article>
</section>
<section class="news">
  <span class="news-icon"></span>
  <h3>LATEST NEWS</h3>
  <p>Temporibus debitis amat aut rerum Itaque earum rerum hic tenetur a sapiente delectus, ut aut reiciendis voluptatibus maiores.</p>
</section>
<footer class="site-footer">
  <nav class="footer-nav"><a href="#">Home</a><span>|</span><a href="#">About</a><span>|</span><a href="#">Associations</a><span>|</span><a href="#">Products</a><span>|</span><a href="#">Calendar</a><span>|</span><a href="#">Offer</a><span>|</span><a href="#">Comments</a><span>|</span><a href="#">Membership</a><span>|</span><a href="#">Contact</a></nav>
  <p class="copyright">Copyright &copy; 2013 &nbsp;www.themarbleatlashub.example &nbsp; All rights reserved.</p>
  <div class="social"><span class="s1"></span><span class="s2"></span></div>
</footer>
</body>
</html>
```